7TallHarbor.com - website redesign

We need to redesign 7TallHarbor.com.
Here are design specs: https://files.quillmarsh.net/deck/8hRkw2LpZn4QvTs0YbXe6MuAcJd9FgNo3WiKl/view?mode=shared

Here is a video going over the design specs:
https://media.quillmarsh.net/clip/d/9x47ruQmTb3HnKcWvZ8oEsYa2LfJ-/play?mode=shared
Updates

I am moving houses on June 10th. Movers are already scheduled.

Target Market(s)

Seattle, WA

Number of Pages Required

2 page

Font styles to use
Serif

Colors

Designer to choose colors to be used in the design.

Requirements
Must have
• Desktop and Mobile Designs
Use colors from their logo....as provided in the design specs document.

Should not have
• Please follow design specs as provided in Google Slides. Must watch the video to understand what's needed.

```html
<!DOCTYPE html>
<html lang="en">
<head>
<meta charset="utf-8">
<title>7TallHarbor.com – Certified E-Recycling</title>
<link href="https://fonts.googleapis.com/css2?family=Montserrat:wght@500;600;700;800&family=Open+Sans:wght@400;600;700&display=swap" rel="stylesheet">
<style>
:root{
  --green:#2e9a3e;
  --green-dark:#1f6e2b;
  --green-deep:#173d1f;
  --ink:#333;
  --muted:#777;
  --line:#dcdcdc;
  --paper:#fff;
  --ghost:#eef1ee;
}
*{box-sizing:border-box;margin:0;padding:0}
html,body{width:1200px;height:2560px;overflow:hidden;background:var(--paper)}
body{font-family:"Open Sans",Arial,sans-serif;color:var(--ink);position:relative}
h1,h2,h3,h4{font-family:"Montserrat",Arial,sans-serif}

/* header */
.site-header{position:absolute;left:0;top:0;width:1200px;z-index:3;background:#fff}
.topbar{height:56px;display:flex;align-items:center;justify-content:space-between;padding:0 80px 0 40px}
.brand{display:flex;align-items:center;gap:10px;font-family:"Montserrat",sans-serif;font-weight:700;font-size:20px;color:var(--green)}
.brand .dot{width:36px;height:36px;border-radius:50%;background:var(--green)}
.top-actions{display:flex;gap:10px}
.pill{font-size:11px;font-weight:600;color:#fff;background:var(--green);padding:6px 14px;border-radius:3px;border:1px solid var(--green)}
.pill.ghost{background:#fff;color:var(--green)}
.mainnav{height:30px;background:var(--green);display:flex;align-items:center;justify-content:space-around;padding:0 70px 0 110px}
.mainnav a{color:#fff;text-decoration:none;font-size:12px;font-weight:600}

/* hero */
.hero{position:absolute;left:0;top:86px;width:1200px;height:600px;overflow:hidden}
.hero-photo{position:absolute;inset:0;background:radial-gradient(circle at 72% 28%,#d8eef2 0 12%,#8fc0a8 20%,transparent 34%),linear-gradient(120deg,#3f6f2a 0%,#6fa04a 40%,#2e5a23 70%,#4d3a22 100%)}
.hero-copy{position:absolute;left:84px;top:62px;color:#fff;width:620px}
.hero-copy h1{font-size:42px;line-height:1.15;font-weight:800}
.hero-copy p{font-size:16px;margin:14px 0 24px;line-height:1.45;width:440px}
.btn{display:inline-block;font-size:11px;font-weight:700;color:#fff;border:1px solid #fff;padding:8px 20px;border-radius:3px}
.hero-wave{position:absolute;left:0;bottom:0;width:1200px;height:200px}

/* services */
.services{position:absolute;left:0;top:712px;width:1200px;display:flex;justify-content:center;gap:32px}
.card{width:312px;background:#fff;box-shadow:0 4px 16px rgba(0,0,0,.12);border-radius:4px;overflow:hidden}
.card-photo{height:120px}
.card-body{padding:18px 20px 22px;position:relative}
.card-icon{position:absolute;top:-24px;left:18px;width:44px;height:44px;border-radius:50%;background:#fff;border:2px solid var(--green);display:flex;align-items:center;justify-content:center}
.card h3{font-size:16px;color:var(--green);margin:24px 0 8px}
.card p{font-size:12px;color:var(--muted);line-height:1.5}
.card .more{display:block;font-size:11px;font-weight:700;color:var(--green);margin-top:12px}

/* process band */
.process{position:absolute;top:1088px;left:0;width:1200px;height:480px;background:radial-gradient(ellipse at 50% 70%,#5b7f3a 0,#2d4e22 40%,var(--green-deep) 80%);color:#fff}
.process h2{position:absolute;left:0;top:62px;width:1200px;text-align:center;font-size:42px;font-weight:700}
.process-path{position:absolute;left:0;top:0}
.step{position:absolute;width:200px;margin-left:-100px;text-align:center;font-size:13px;font-weight:600;line-height:1.35}
.step .ring{width:46px;height:46px;border-radius:50%;border:2px solid #fff;background:rgba(255,255,255,.1);margin:0 auto 10px;display:flex;align-items:center;justify-content:center}

/* about */
.about{position:absolute;top:1600px;left:0;width:1200px;height:460px}
.about-word{position:absolute;left:14px;top:96px;writing-mode:vertical-rl;transform:rotate(180deg);font-family:"Montserrat",sans-serif;font-size:84px;font-weight:800;color:var(--ghost);letter-spacing:6px;line-height:1}
.about-copy{position:absolute;left:170px;top:60px;width:330px}
.about-copy h2{font-size:30px;color:var(--green);margin-bottom:14px}
.about-copy p{font-size:11px;color:var(--muted);line-height:1.55;margin-bottom:10px}
.about-copy h4{font-size:12px;color:var(--green);margin:6px 0 6px}
.stats{display:flex;gap:18px;margin-bottom:20px}
.stats div{font-size:10px;color:var(--muted)}
.stats b{display:block;font-family:"Montserrat",sans-serif;font-size:14px;color:var(--ink)}
.about-actions{display:flex;gap:12px}
.about-actions .btn{background:var(--green);border-color:var(--green)}
.about-photo{position:absolute;left:520px;top:128px;width:608px;height:320px;background:linear-gradient(135deg,#d2d2d2,#707070 55%,#2e2e2e)}

/* contact */
.contact{position:absolute;top:2040px;left:0;width:1200px;height:470px}
.map{position:absolute;left:88px;top:20px;width:592px;height:400px;background:linear-gradient(160deg,#eceee8,#e2e6dc 50%,#f2ede0)}
.form{position:absolute;left:688px;top:0;width:432px;background:#fff;box-shadow:0 4px 16px rgba(0,0,0,.1);padding:24px 28px}
.form h2{font-size:30px;color:var(--green);text-align:center;margin-bottom:18px}
.row{display:flex;gap:10px;margin-bottom:10px}
.field{flex:1;height:32px;border:1px solid var(--line);font-size:11px;color:var(--muted);padding:8px 10px}
.checks{border:1px solid var(--line);padding:8px 10px;margin-bottom:10px}
.checks div{font-size:11px;color:var(--ink);display:flex;align-items:center;gap:8px;margin:4px 0}
.checks span{width:10px;height:10px;border:1px solid #999}
.message{height:66px;border:1px solid var(--line);font-size:11px;color:var(--muted);padding:8px 10px;margin-bottom:12px}
.submit{background:var(--green);color:#fff;text-align:center;font-size:12px;font-weight:700;padding:9px}
</style>
</head>
<body>

<header class="site-header">
  <div class="topbar">
    <div class="brand"><span class="dot"></span>7TallHarbor.com</div>
    <div class="top-actions">
      <span class="pill">(206) 555-0148</span>
      <span class="pill">hello@7tallharbor.com</span>
      <span class="pill ghost">Get a Quote</span>
      <span class="pill">Drop Off</span>
    </div>
  </div>
  <nav class="mainnav">
    <a>E-Waste Disposal</a><a>Electronics Recycling</a><a>Secure Data Destruction</a><a>Product Destruction</a><a>About</a><a>Contact Us</a>
  </nav>
</header>

<section class="hero">
  <div class="hero-photo" role="img" aria-label="Glass globe resting in green grass and leaves"></div>
  <div class="hero-copy">
    <h1>Certified E-Recycling<br>Made Easy</h1>
    <p>Reuse &amp; Recycle 99.9% of all electronics we receive</p>
    <span class="btn">Learn More</span>
  </div>
  <svg class="hero-wave" viewBox="0 0 1200 200" preserveAspectRatio="none">
    <path d="M0 90 C300 200 700 120 1200 20 L1200 200 L0 200Z" fill="#2e9a3e"/>
    <path d="M0 150 C350 230 800 150 1200 90 L1200 200 L0 200Z" fill="#fff"/>
  </svg>
</section>

<section class="services">
  <article class="card">
    <div class="card-photo" role="img" aria-label="Recycling bin for electronic waste" style="background:linear-gradient(135deg,#5d7fa8,#2f5480)"></div>
    <div class="card-body">
      <div class="card-icon"><svg width="20" height="20" viewBox="0 0 24 24" fill="none" stroke="#2e9a3e" stroke-width="2"><path d="M5 7h14l-1.5 14h-11z M9 7V4h6v3"/></svg></div>
      <h3>BIN Program</h3>
      <p>Fill up our bins at your location, and we swap them out on a schedule that suits you.</p>
      <span class="more">Learn more</span>
    </div>
  </article>
  <article class="card">
    <div class="card-photo" role="img" aria-label="Hands passing a cardboard box for pickup" style="background:linear-gradient(135deg,#cdb597,#9c7d5c)"></div>
    <div class="card-body">
      <div class="card-icon"><svg width="20" height="20" viewBox="0 0 24 24" fill="none" stroke="#2e9a3e" stroke-width="2"><circle cx="12" cy="12" r="9"/><path d="M8 12l3 3 5-6"/></svg></div>
      <h3>Same Day Pickups Available</h3>
      <p>Call before noon and our team can collect your items from your site that same day.</p>
      <span class="more">Learn more</span>
    </div>
  </article>
  <article class="card">
    <div class="card-photo" role="img" aria-label="Row of recycling containers against a wall" style="background:linear-gradient(135deg,#a9b3ad,#6f7b74)"></div>
    <div class="card-body">
      <div class="card-icon"><svg width="20" height="20" viewBox="0 0 24 24" fill="none" stroke="#2e9a3e" stroke-width="2"><path d="M12 3l8 3v6c0 5-4 8-8 9-4-1-8-4-8-9V6z"/></svg></div>
      <h3>On-site Data Destruction</h3>
      <p>We wipe and destroy drives at your location so your data never leaves your sight.</p>
      <span class="more">Learn more</span>
    </div>
  </article>
</section>

<section class="process" role="img" aria-label="Hands holding a young plant over soil">
  <h2>Save time. Save money. Save the planet.</h2>
  <svg class="process-path" width="1200" height="480">
    <path d="M188 235 C260 235 300 345 380 345 C470 345 500 235 588 235 C680 235 720 345 820 345 C900 345 930 235 1012 235" fill="none" stroke="#fff" stroke-width="2" stroke-dasharray="5 6"/>
  </svg>
  <div class="step" style="left:188px;top:212px"><div class="ring"><svg width="20" height="20" viewBox="0 0 24 24" fill="none" stroke="#fff" stroke-width="2"><path d="M5 4h4l2 5-2.5 1.5a11 11 0 005 5L15 13l5 2v4a2 2 0 01-2 2A16 16 0 013 6a2 2 0 012-2z"/></svg></div>Quick Response</div>
  <div class="step" style="left:380px;top:322px"><div class="ring"><svg width="20" height="20" viewBox="0 0 24 24" fill="none" stroke="#fff" stroke-width="2"><rect x="4" y="5" width="16" height="15" rx="1"/><path d="M4 10h16M8 3v4M16 3v4"/></svg></div>Immediate Scheduling</div>
  <div class="step" style="left:588px;top:212px"><div class="ring"><svg width="20" height="20" viewBox="0 0 24 24" fill="none" stroke="#fff" stroke-width="2"><circle cx="12" cy="13" r="8"/><path d="M12 9v4l3 2M10 3h4"/></svg></div>On-time<br>Secure Pickup</div>
  <div class="step" style="left:820px;top:322px"><div class="ring"><svg width="20" height="20" viewBox="0 0 24 24" fill="none" stroke="#fff" stroke-width="2"><path d="M12 3l8 3v6c0 5-4 8-8 9-4-1-8-4-8-9V6z"/><path d="M8.5 12l2.5 2.5 4.5-5"/></svg></div>Certified Recycling Process</div>
  <div class="step" style="left:1012px;top:212px"><div class="ring"><svg width="20" height="20" viewBox="0 0 24 24" fill="none" stroke="#fff" stroke-width="2"><circle cx="12" cy="9" r="5"/><path d="M9 13l-2 8 5-3 5 3-2-8"/></svg></div>Certifications &amp;<br>Asset Tracking Delivered</div>
</section>

<section class="about">
  <div class="about-word">ABOUT</div>
  <div class="about-copy">
    <h2>About Us</h2>
    <p>We are electronic recyclers who care deeply about reducing waste and helping our community keep devices out of landfills.</p>
    <p>Founded in Seattle, our certified team handles everything from a single laptop to full office cleanouts, with secure tracking every step of the way.</p>
    <h4>Pounds Recycled</h4>
    <div class="stats">
      <div><b>2 Million</b>Electronics</div>
      <div><b>1 Million</b>Computers</div>
      <div><b>500K</b>Drives</div>
      <div><b>30K</b>Clients</div>
    </div>
    <div class="about-actions"><span class="btn">Read More</span><span class="btn">Schedule Pickup</span></div>
  </div>
  <div class="about-photo" role="img" aria-label="Workers sorting electronics in a recycling warehouse"></div>
</section>

<section class="contact">
  <div class="map" role="img" aria-label="Street map showing the facility location"></div>
  <div class="form">
    <h2>Contact Us</h2>
    <div class="row"><div class="field">Name</div><div class="field">Phone</div></div>
    <div class="row"><div class="field">Email</div></div>
    <div class="checks">
      <div><span></span>Electronics Recycling</div>
      <div><span></span>Equipment &amp; Product Destruction</div>
      <div><span></span>Secure Data Destruction</div>
      <div><span></span>IT Asset Disposition</div>
    </div>
    <div class="message">Message</div>
    <div class="submit">SUBMIT</div>
  </div>
</section>

</body>
</html>
```